Design an investor pitch deck for Brindlework.io

We delivered a killer investor pitch to a group of investors last week and have been asked for a deck. we need to follow up with a killer printed version. I have produced the attached file using free images from fotovane. Feel free to change the imagery as you see fit. Check out brindlework.io to get a feel for the look and feel we have right now.

Target Market(s)

Investors

Industry/Entity Type

Software

Font styles to use
Sans Serif
Other font styles liked:
• Helvetica

Requirements
Must have
• A new version of each of the pages in the example documents. Needs to be slick and professional
Nice to have
• Other layouts in case I add further slides
Should not have
• Childish or dated shapes or designs

```html
<!DOCTYPE html>
<html lang="en">
<head>
<meta charset="utf-8">
<title>Brindlework.io — Additional Templates</title>
<link rel="stylesheet" href="https://fonts.googleapis.com/css2?family=Montserrat:wght@300;400;500;600;700&family=Open+Sans:wght@700;800&display=swap">
<style>
:root{
  --navy:#2b3467;
  --yellow:#f5c531;
  --slate:#626262;
  --ink:#1b1b1b;
  --muted:#8a8a8a;
  --faint:#ececec;
  --page:#b7b7b7;
  --card:#ffffff;
  --sheet:#f1f1f3;
}
*{box-sizing:border-box;margin:0;padding:0}
html,body{width:1200px;height:1060px;overflow:hidden}
body{background:var(--page);font-family:'Montserrat',Helvetica,Arial,sans-serif;position:relative;color:var(--ink)}
.page-number{position:absolute;left:6px;top:5px;font:700 13px 'Open Sans',Arial,sans-serif;color:#2454c7}
.sheet-title{position:absolute;left:0;width:1170px;top:110px;text-align:center;font:700 35px 'Open Sans',Arial,sans-serif;letter-spacing:.2px;color:#000}
.slide{position:absolute;width:354px;height:199px;background:var(--card);overflow:hidden}
.slide-title{position:absolute;left:0;right:0;top:20px;text-align:center;font-weight:400;font-size:20px;letter-spacing:1.6px;color:var(--ink)}
.slide svg.body{position:absolute;left:0;top:0;width:354px;height:199px}
.slide-url{position:absolute;left:16px;bottom:6px;font-size:3.5px;color:#bbb}
.slide-brand{position:absolute;right:11px;bottom:5px;font-size:7.5px;font-weight:700;letter-spacing:.6px;color:var(--ink)}
svg text{font-family:'Montserrat',Helvetica,Arial,sans-serif}
.tiny{font-size:3.6px;fill:var(--muted)}
.head{font-size:4.6px;font-weight:700;fill:var(--navy)}
</style>
</head>
<body>
<div class="page-number">24</div>
<h1 class="sheet-title">Some Additional Templates</h1>

<!-- Icons and text -->
<section class="slide" style="left:34px;top:208px">
  <h2 class="slide-title">ICONS AND TEXT</h2>
  <svg class="body" viewBox="0 0 354 199">
    <g fill="none" stroke-width="5.5">
      <circle cx="90" cy="92" r="33" stroke="var(--navy)"/>
      <circle cx="152" cy="92" r="33" stroke="var(--yellow)"/>
      <circle cx="214" cy="92" r="33" stroke="var(--navy)"/>
      <circle cx="277" cy="92" r="33" stroke="var(--yellow)"/>
    </g>
    <g fill="none" stroke-width="1" stroke-linecap="round" stroke-linejoin="round">
      <path d="M84 92h-2a4 4 0 0 1 0-8 6 6 0 0 1 11-1 3.5 3.5 0 0 1 1 9h-2 M88 88v8 M86 94l2 2 2-2" stroke="var(--navy)"/>
      <path d="M148 80h5l3 3v10h-8z M152 84v5 M149.5 86.5h5" stroke="var(--yellow)"/>
      <path d="M209 92v-5a5 5 0 0 1 10 0v5l1.5 2h-13z M212.5 95.5a1.5 1.5 0 0 0 3 0" stroke="var(--navy)"/>
      <rect x="270" y="82" width="14" height="9" rx="2" stroke="var(--yellow)"/>
      <path d="M273 91l-1 3 4-3" stroke="var(--yellow)"/>
    </g>
    <g fill="var(--yellow)"><circle cx="274" cy="86.5" r=".8"/><circle cx="277" cy="86.5" r=".8"/><circle cx="280" cy="86.5" r=".8"/></g>
    <g font-size="2.6" font-weight="700" text-anchor="middle">
      <text x="90" y="102" fill="var(--navy)">LOREM IPSUM</text>
      <text x="152" y="102" fill="var(--yellow)">LOREM IPSUM</text>
      <text x="214" y="102" fill="var(--navy)">LOREM IPSUM</text>
      <text x="277" y="102" fill="var(--yellow)">LOREM IPSUM</text>
    </g>
    <g class="tiny" text-anchor="middle">
      <text x="177" y="144">Iste natus error sit voluptatem accusantium doloremque laudantium, totam rem aperiam, eaque ipsa quae ab illo inventore veritatis</text>
      <text x="177" y="149">et quasi architecto beatae vitae dicta sunt explicabo. Nemo enim ipsam voluptatem quia voluptas sit aspernatur aut odit aut fugit,</text>
      <text x="177" y="154">sed quia consequuntur magni dolores eos qui ratione voluptatem sequi nesciunt. Neque porro quisquam est, qui dolorem ipsum</text>
      <text x="177" y="159">quia dolor sit amet, consectetur, adipisci velit, commodi consequatur</text>
    </g>
  </svg>
  <span class="slide-url">www.brindlework.io</span>
  <span class="slide-brand">BRINDLEWORK</span>
</section>

<!-- Content slide numbered -->
<section class="slide" style="left:411px;top:208px">
  <h2 class="slide-title">CONTENT SLIDE</h2>
  <svg class="body" viewBox="0 0 354 199">
    <g font-size="38" font-weight="300" fill="var(--faint)">
      <text x="27" y="121">01</text><text x="189" y="121">02</text>
      <text x="27" y="177">03</text><text x="189" y="177">04</text>
    </g>
    <g>
      <text class="head" x="82" y="89">LOREM IPSUM DOLOR</text>
      <text class="tiny" x="82" y="97">Lorem ipsum dolor sit amet, consec-</text>
      <text class="tiny" x="82" y="102">tetur adipiscing elit, sed do eiusmod</text>
      <text class="tiny" x="82" y="107">tempor incididunt ut labore et dolore</text>
      <text class="tiny" x="82" y="112">magna aliqua.</text>
      <text class="head" x="246" y="89">LOREM IPSUM DOLOR</text>
      <text class="tiny" x="246" y="97">Lorem ipsum dolor sit amet, consec-</text>
      <text class="tiny" x="246" y="102">tetur adipiscing elit, sed do eiusmod</text>
      <text class="tiny" x="246" y="107">tempor incididunt ut labore et dolore</text>
      <text class="tiny" x="246" y="112">magna aliqua.</text>
      <text class="head" x="82" y="145">LOREM IPSUM DOLOR</text>
      <text class="tiny" x="82" y="153">Lorem ipsum dolor sit amet, consec-</text>
      <text class="tiny" x="82" y="158">tetur adipiscing elit, sed do eiusmod</text>
      <text class="tiny" x="82" y="163">tempor incididunt ut labore et dolore</text>
      <text class="tiny" x="82" y="168">magna aliqua.</text>
      <text class="head" x="246" y="145">LOREM IPSUM DOLOR</text>
      <text class="tiny" x="246" y="153">Lorem ipsum dolor sit amet, consec-</text>
      <text class="tiny" x="246" y="158">tetur adipiscing elit, sed do eiusmod</text>
      <text class="tiny" x="246" y="163">tempor incididunt ut labore et dolore</text>
      <text class="tiny" x="246" y="168">magna aliqua.</text>
    </g>
  </svg>
  <span class="slide-url">www.brindlework.io</span>
  <span class="slide-brand">BRINDLEWORK</span>
</section>

<!-- Team slide -->
<section class="slide" style="left:790px;top:208px">
  <h2 class="slide-title">TEAM SLIDE</h2>
  <svg class="body" viewBox="0 0 354 199">
    <defs>
      <radialGradient id="portrait" cx=".5" cy=".4" r=".6">
        <stop offset="0" stop-color="#8d8d8d"/><stop offset="1" stop-color="#4a4a4a"/>
      </radialGradient>
      <g id="member">
        <circle cx="0" cy="0" r="14" fill="url(#portrait)" role="img" aria-label="Team member portrait"/>
        <text x="20" y="-7" font-size="4.6" fill="var(--navy)">Josh Doe</text>
        <text x="20" y="-2.5" font-size="2.4" font-weight="700" fill="var(--ink)">EXECUTIVE DIRECTOR</text>
        <text x="20" y="1.5" font-size="2.2" fill="var(--muted)">Lorem ipsum dolor sit amet consecte</text>
        <text x="20" y="4.5" font-size="2.2" fill="var(--muted)">tur adipiscing elit, sed do eiusmod</text>
        <text x="20" y="7.5" font-size="2.2" fill="var(--muted)">tempor incididunt ut labore et dolore</text>
        <text x="20" y="10.5" font-size="2.2" fill="var(--muted)">magna aliqua.</text>
      </g>
    </defs>
    <use href="#member" x="45" y="78"/><use href="#member" x="153" y="78"/><use href="#member" x="261" y="78"/>
    <use href="#member" x="45" y="128"/><use href="#member" x="153" y="128"/><use href="#member" x="261" y="128"/>
    <g stroke="#eee" stroke-width=".5"><line x1="122" y1="64" x2="122" y2="145"/><line x1="230" y1="64" x2="230" y2="145"/></g>
  </svg>
  <span class="slide-url">www.brindlework.io</span>
  <span class="slide-brand">BRINDLEWORK</span>
</section>

<!-- Image and text, three columns -->
<section class="slide" style="left:34px;top:435px">
  <h2 class="slide-title">IMAGE AND TEXT SLIDE</h2>
  <svg class="body" viewBox="0 0 354 199">
    <defs>
      <linearGradient id="port" x1="0" y1="0" x2="0" y2="1">
        <stop offset="0" stop-color="#e4e4e4"/><stop offset=".6" stop-color="#a9a9a9"/><stop offset="1" stop-color="#4d4d4d"/>
      </linearGradient>
    </defs>
    <g role="img" aria-label="Black and white photo of harbour cranes">
      <rect x="32" y="70" width="90" height="47" fill="url(#port)"/>
      <rect x="133.5" y="70" width="90" height="47" fill="url(#port)"/>
      <rect x="235" y="70" width="90" height="47" fill="url(#port)"/>
    </g>
    <g>
      <text class="head" x="32" y="127">LOREM IPSUM DOLOR</text>
      <rect x="32" y="130" width="18" height="1.3" fill="var(--navy)"/>
      <text class="tiny" x="32" y="137">Lorem ipsum dolor sit amet, consectetur</text>
      <text class="tiny" x="32" y="141.5">adipiscing elit, sed do eiusmod tempor</text>
      <text class="tiny" x="32" y="146">incididunt ut labore et dolore magna aliqua.</text>
      <text class="head" x="133.5" y="127">LOREM IPSUM DOLOR</text>
      <rect x="133.5" y="130" width="18" height="1.3" fill="var(--navy)"/>
      <text class="tiny" x="133.5" y="137">Lorem ipsum dolor sit amet, consectetur</text>
      <text class="tiny" x="133.5" y="141.5">adipiscing elit, sed do eiusmod tempor</text>
      <text class="tiny" x="133.5" y="146">incididunt ut labore et dolore magna aliqua.</text>
      <text class="head" x="235" y="127">LOREM IPSUM DOLOR</text>
      <rect x="235" y="130" width="18" height="1.3" fill="var(--navy)"/>
      <text class="tiny" x="235" y="137">Lorem ipsum dolor sit amet, consectetur</text>
      <text class="tiny" x="235" y="141.5">adipiscing elit, sed do eiusmod tempor</text>
      <text class="tiny" x="235" y="146">incididunt ut labore et dolore magna aliqua.</text>
    </g>
  </svg>
  <span class="slide-url">www.brindlework.io</span>
  <span class="slide-brand">BRINDLEWORK</span>
</section>

<!-- Image and text, devices -->
<section class="slide" style="left:411px;top:435px">
  <h2 class="slide-title">IMAGE AND TEXT SLIDE</h2>
  <svg class="body" viewBox="0 0 354 199">
    <defs>
      <linearGradient id="devices" x1="0" y1="0" x2="1" y2="1">
        <stop offset="0" stop-color="#2a2a2a"/><stop offset="1" stop-color="#0c0c0c"/>
      </linearGradient>
    </defs>
    <rect x="45" y="70" width="158" height="78" rx="3" fill="url(#devices)" role="img" aria-label="Product mockup on desktop, laptop, tablet and phone screens"/>
    <g font-size="6" fill="#7a7a7a">
      <text x="221" y="78">Nemo enim ipsam voluptatem quia</text>
      <text x="221" y="86">voluptas sit aspernatur aut odit aut</text>
      <text x="221" y="94">fugit, sed quia consequuntur</text>
      <text x="221" y="102">magni dolores eos qui ratione vo-</text>
      <text x="221" y="110">luptatem sequi nesciunt. Neque</text>
      <text x="221" y="118">porro quisquam est, qui dolorem</text>
      <text x="221" y="126">ipsum quia dolor sit amet, consec-</text>
      <text x="221" y="134">tetur, adipisci velit, commodi con-</text>
      <text x="221" y="142">sequatur</text>
    </g>
  </svg>
  <span class="slide-url">www.brindlework.io</span>
  <span class="slide-brand">BRINDLEWORK</span>
</section>

<!-- Pricing -->
<section class="slide" style="left:786px;top:435px">
  <h2 class="slide-title">PRICING SLIDE</h2>
  <svg class="body" viewBox="0 0 354 199">
    <defs>
      <g id="features">
        <text y="0">CONSECTETUR ADIPISCING ELIT</text>
        <text y="9">CONSECTETUR ADIPISCING ELIT</text>
        <text y="18">CONSECTETUR ADIPISCING ELIT</text>
        <text y="27">CONSECTETUR ADIPISCING ELIT</text>
      </g>
    </defs>
    <rect x="68" y="66" width="63" height="95" fill="var(--sheet)"/>
    <rect x="68" y="66" width="63" height="11" fill="var(--navy)"/>
    <rect x="139" y="58" width="76" height="112" fill="var(--sheet)"/>
    <rect x="139" y="58" width="76" height="14" fill="var(--yellow)"/>
    <rect x="223" y="66" width="63" height="95" fill="var(--sheet)"/>
    <rect x="223" y="66" width="63" height="11" fill="var(--slate)"/>
    <g font-size="2.8" font-weight="700" fill="#fff" text-anchor="middle">
      <text x="99.5" y="73">LOREM IPSUM DOLOR</text>
      <text x="177" y="66.5">LOREM IPSUM DOLOR</text>
      <text x="254.5" y="73">LOREM IPSUM DOLOR</text>
    </g>
    <g font-size="3.3" font-weight="500" fill="var(--ink)" text-anchor="middle">
      <text x="99.5" y="84">30 DAYS FREE TRIAL</text>
      <text x="177" y="79">30 DAYS FREE TRIAL</text>
      <text x="254.5" y="84">30 DAYS FREE TRIAL</text>
    </g>
    <g fill="var(--ink)" font-weight="300">
      <text x="86" y="99" font-size="16">12<tspan font-size="8">/mo</tspan></text>
      <text x="81" y="93" font-size="5">$</text>
      <text x="161" y="96" font-size="19">12<tspan font-size="9.5">/mo</tspan></text>
      <text x="155" y="89" font-size="6">$</text>
      <text x="241" y="99" font-size="16">12<tspan font-size="8">/mo</tspan></text>
      <text x="236" y="93" font-size="5">$</text>
    </g>
    <g font-size="2.2" fill="var(--muted)" text-anchor="middle">
      <use href="#features" x="99.5" y="110"/>
      <use href="#features" x="254.5" y="110"/>
    </g>
    <g font-size="2.5" fill="var(--muted)" text-anchor="middle">
      <text x="177" y="112">CONSECTETUR ADIPISCING ELIT</text>
      <text x="177" y="123">CONSECTETUR ADIPISCING ELIT</text>
      <text x="177" y="134">CONSECTETUR ADIPISCING ELIT</text>
      <text x="177" y="145">CONSECTETUR ADIPISCING ELIT</text>
    </g>
    <g fill="#fff" stroke="#d4d4d4" stroke-width=".4">
      <rect x="88" y="149" width="23" height="5"/>
      <rect x="163" y="158" width="28" height="6"/>
      <rect x="243" y="149" width="23" height="5"/>
    </g>
    <g font-size="2" fill="var(--muted)" text-anchor="middle">
      <text x="99.5" y="152.3">SELECT PLAN</text>
      <text x="177" y="161.7">SELECT PLAN</text>
      <text x="254.5" y="152.3">SELECT PLAN</text>
    </g>
  </svg>
  <span class="slide-url">www.brindlework.io</span>
  <span class="slide-brand">BRINDLEWORK</span>
</section>

<!-- Table -->
<section class="slide" style="left:34px;top:674px">
  <h2 class="slide-title">TABLE SLIDE</h2>
  <svg class="body" viewBox="0 0 354 199">
    <rect x="57" y="57" width="241" height="106" fill="#fff" stroke="#e2e2e2" stroke-width=".6"/>
    <rect x="57" y="57" width="96" height="24" fill="var(--slate)"/>
    <rect x="153" y="57" width="73" height="24" fill="var(--yellow)"/>
    <rect x="226" y="57" width="72" height="24" fill="var(--navy)"/>
    <g font-size="4.6" font-weight="500" fill="#fff">
      <text x="65" y="71">CATEGORY</text>
      <text x="173" y="71">COLUMN 1</text>
      <text x="245" y="71">COLUMN 2</text>
    </g>
    <g stroke="#e8e8e8" stroke-width=".5">
      <line x1="153" y1="81" x2="153" y2="163"/><line x1="226" y1="81" x2="226" y2="163"/>
      <line x1="162" y1="102" x2="218" y2="102"/><line x1="162" y1="113" x2="218" y2="113"/><line x1="162" y1="124.5" x2="218" y2="124.5"/><line x1="162" y1="136" x2="218" y2="136"/>
      <line x1="234" y1="102" x2="290" y2="102"/><line x1="234" y1="113" x2="290" y2="113"/><line x1="234" y1="124.5" x2="290" y2="124.5"/><line x1="234" y1="136" x2="290" y2="136"/>
    </g>
    <g font-size="3.4" fill="#777">
      <text x="65" y="99">SED UT PERSPICIATIS UNDE OMNIS</text>
      <text x="65" y="110">SED UT PERSPICIATIS UNDE OMNIS</text>
      <text x="65" y="121.5">SED UT PERSPICIATIS UNDE OMNIS</text>
      <text x="65" y="133">SED UT PERSPICIATIS UNDE OMNIS</text>
      <text x="65" y="144">SED UT PERSPICIATIS UNDE OMNIS</text>
    </g>
    <g font-size="3.4" fill="#777" text-anchor="middle">
      <text x="189.5" y="99">VOLUPTATEM</text><text x="189.5" y="110">VOLUPTATEM</text><text x="189.5" y="121.5">VOLUPTATEM</text><text x="189.5" y="133">VOLUPTATEM</text><text x="189.5" y="144">VOLUPTATEM</text>
      <text x="262" y="99">VOLUPTATEM</text><text x="262" y="110">VOLUPTATEM</text><text x="262" y="121.5">VOLUPTATEM</text><text x="262" y="133">VOLUPTATEM</text><text x="262" y="144">VOLUPTATEM</text>
    </g>
  </svg>
  <span class="slide-url">www.brindlework.io</span>
  <span class="slide-brand">BRINDLEWORK</span>
</section>

<!-- Pie chart -->
<section class="slide" style="left:411px;top:674px">
  <h2 class="slide-title">PIE CHART SLIDE</h2>
  <svg class="body" viewBox="0 0 354 199">
    <path d="M252 56A54 54 0 0 1 252 164V134A24 24 0 0 0 252 86Z" fill="var(--yellow)"/>
    <path d="M252 164A54 54 0 0 1 198 110H228A24 24 0 0 0 252 134Z" fill="var(--navy)"/>
    <path d="M198 110A54 54 0 0 1 252 56V86A24 24 0 0 0 228 110Z" fill="var(--slate)"/>
    <line x1="252" y1="56" x2="252" y2="164" stroke="#fff" stroke-width="1.2"/>
    <line x1="198" y1="110" x2="252" y2="110" stroke="#fff" stroke-width="1.2"/>
    <circle cx="252" cy="110" r="23" fill="#fff"/>
    <g fill="none" stroke="var(--ink)" stroke-width=".9" stroke-linejoin="round">
      <rect x="243" y="105" width="18" height="12" rx="1.5"/>
      <path d="M249 105v-2.5h6v2.5 M243 110.5h18 M251 109.5v2h2v-2"/>
    </g>
    <g font-size="7" font-weight="300" fill="#fff" text-anchor="middle">
      <text x="219" y="89">25%</text>
      <text x="219" y="136">25%</text>
      <text x="290" y="113">50%</text>
    </g>
    <circle cx="70" cy="71" r="10" fill="var(--slate)"/>
    <circle cx="70" cy="109" r="10" fill="var(--yellow)"/>
    <circle cx="70" cy="146" r="10" fill="var(--navy)"/>
    <g font-size="5" fill="#fff" text-anchor="middle">
      <text x="70" y="72.7">25%</text><text x="70" y="110.7">50%</text><text x="70" y="147.7">25%</text>
    </g>
    <g>
      <text x="85" y="67" font-size="3.6" font-weight="700" fill="var(--ink)">LOREM IPSUM DOLOR</text>
      <text class="tiny" x="85" y="73">Lorem ipsum dolor sit amet, consectetur</text>
      <text class="tiny" x="85" y="77">adipiscing elit, sed do eiusmod tempor inci-</text>
      <text class="tiny" x="85" y="81">dunt ut labore et dolore magna aliqua</text>
      <text x="85" y="104" font-size="3.6" font-weight="700" fill="var(--ink)">LOREM IPSUM DOLOR</text>
      <text class="tiny" x="85" y="110">Lorem ipsum dolor sit amet, consectetur</text>
      <text class="tiny" x="85" y="114">adipiscing elit, sed do eiusmod tempor inci-</text>
      <text class="tiny" x="85" y="118">dunt ut labore et dolore magna aliqua</text>
      <text x="85" y="141" font-size="3.6" font-weight="700" fill="var(--ink)">LOREM IPSUM DOLOR</text>
      <text class="tiny" x="85" y="147">Lorem ipsum dolor sit amet, consectetur</text>
      <text class="tiny" x="85" y="151">adipiscing elit, sed do eiusmod tempor inci-</text>
      <text class="tiny" x="85" y="155">dunt ut labore et dolore magna aliqua</text>
    </g>
  </svg>
  <span class="slide-url">www.brindlework.io</span>
  <span class="slide-brand">BRINDLEWORK</span>
</section>

<!-- Content slide, coloured cards -->
<section class="slide" style="left:786px;top:674px">
  <h2 class="slide-title">CONTENT SLIDE</h2>
  <svg class="body" viewBox="0 0 354 199">
    <defs>
      <g id="card-copy" font-size="3.2" text-anchor="middle">
        <text y="0" font-weight="700" font-size="3.6">LOREM IPSUM DOLOR</text>
        <text y="8">Lorem ipsum dolor sit amet,</text>
        <text y="12">consectetur adipiscing elit,</text>
        <text y="16">sed do eiusmod tempor</text>
        <text y="20">incididunt ut labore et dolore</text>
        <text y="24">magna aliqua. Ut enim ad</text>
        <text y="28">minim veniam, quis nostrud</text>
        <text y="32">exercitation</text>
      </g>
    </defs>
    <rect x="50" y="68" width="68" height="91" fill="var(--navy)"/>
    <rect x="144" y="68" width="68" height="91" fill="var(--slate)"/>
    <rect x="236" y="68" width="68" height="91" fill="var(--yellow)"/>
    <g fill="#fff"><circle cx="84" cy="89" r="9"/><circle cx="178" cy="89" r="9"/><circle cx="270" cy="89" r="9"/></g>
    <path d="M80 89.5l8-4-3 8-1.5-3z" fill="none" stroke="var(--navy)" stroke-width=".8" stroke-linejoin="round"/>
    <g fill="none" stroke="var(--slate)" stroke-width=".8"><circle cx="178" cy="89.5" r="4"/><path d="M178 87v2.5l1.5 1 M177 84.5h2"/></g>
    <path d="M267 93l1-3 4.5-4.5 2 2-4.5 4.5z" fill="none" stroke="var(--yellow)" stroke-width=".8" stroke-linejoin="round"/>
    <use href="#card-copy" x="84" y="110" fill="#fff"/>
    <use href="#card-copy" x="178" y="110" fill="#fff"/>
    <use href="#card-copy" x="270" y="110" fill="#fff"/>
  </svg>
  <span class="slide-url">www.brindlework.io</span>
  <span class="slide-brand">BRINDLEWORK</span>
</section>
</body>
</html>
```